The Lune Fox Organic & Natural Soaps needs a good business card

I am sorry for the lack of direction or Scope of the project. I am new at this board.
This is my scope and requirements:
Business card project:
This is related to the Label project I also opened up. (The Lune Fox Organic & Natural Soaps is looking for label designs (along with the business card project (Contest) )
I have attached an initial draft at a logo I tried to come up with for a business card and labelling/marketing. I am hoping that you can take this logo and 'run with it' to finesse it, make it look unique and professional. I am open to new logo ideas.
I am a start up at home company making Organic and Natural Bar soaps, hand soaps, body washes.
All of my ingredients are organic or natural and will include natural essential oils, exfoliants, natural powders/colours, etc.
Some of the names are: Brambelle (feisty, energetic soap), Dunes (more of a sandalwood earthy tones with a sandalwood powder exfoliant), Frost (maybe changing this name - fresh scented), Plum Cedar (lemongrass/ginger, exfoliants), etc....
I am attaching the cardstock I am looking at for packaging as well - this might help with the business card aspect. I was originally just looking at plain kraft paper but am receiving samples of Vera Pindle coloured kraft paper. I may still print business cards on the plain kraft though.. not sure.
If you need more information, please let me know.
Moira
Business Card and Labels
I have come up with a basic logo that I like. If you can finesse it and provide a great business card, that would be great.
I am starting up an at home soap business that will include luxury organic bar soaps, luxury natural olive oil bar soaps, organic hand wash, natural olive oil based body wash. I will be selling online and at shows.
please find attached my logo idea that I would like to incorporate.
I am also looking at packaging/labelling ideas for the bar soaps (prefer kraft cardstock wrap) and labels for the various body washes (natural soap) and the hand washes (organic). The hand washes will be in 250ml square bottles and the body wash will be in tapered bottles (smaller at top going to bottom).
Please let me know if you need more info!
I am also looking for packaging (label design for hand soap/body wash bottles and label design for organic/natural soaps)
This Project coincides with the business card project I also posted: there are 2 projects related - 1) business cards, 2) labels for organic hand wash, natural body wash, sticker label or design for kraft paper to package around luxury organic and natural soaps. I am not sure if a sticker would look nice or the design for the thick kraft paper.
Thank you!
Business card project:
This is related to the Label project I also opened up. (The Lune Fox Organic & Natural Soaps is looking for label designs (along with the business card proje (Contest) )
I have attached an initial draft at a logo I tried to come up with for a business card and labelling/marketing. I am hoping that you can take this logo and 'run with it' to finesse it, make it look unique and professional.
Moira
Hello; I just wanted to let everyone know that if you feel that this
brand needs a different logo, I am open to ideas (if you don't think the
one I started with is ok). I am coming to the experts here!
Just to confirm also - this is related to the label/packaging project, therefore, there are 2 projects, 2 payments! :)
Cheers

```html
<!DOCTYPE html>
<html lang="en">
<head>
<meta charset="utf-8">
<title>The Lune Fox – Business Card</title>
<link rel="stylesheet" href="https://fonts.googleapis.com/css2?family=Dosis:wght@300;400;500;600&display=swap">
<style>
  :root {
    --backdrop: #e9e5e0;
    --kraft: #b99f84;
    --kraft-edge: #a88e73;
    --ink: #221c18;
    --ink-soft: #3a312b;
    --accent-pink: #e6a3ea;
  }
  html, body {
    margin: 0;
    padding: 0;
    width: 1200px;
    height: 1200px;
    overflow: hidden;
    background: var(--backdrop);
  }
  .canvas {
    position: relative;
    width: 1200px;
    height: 1200px;
  }
  .business-card {
    position: absolute;
    left: 100px;
    top: 300px;
    width: 1000px;
    height: 600px;
    font-family: "Dosis", sans-serif;
    color: var(--ink);
  }
  .card-shape {
    position: absolute;
    inset: 0;
    width: 100%;
    height: 100%;
  }
  .brand-block {
    position: absolute;
    left: 60px;
    top: 200px;
    width: 380px;
    text-align: center;
  }
  .brand-mark {
    display: inline-flex;
    align-items: center;
    gap: 14px;
  }
  .brand-dot {
    width: 26px;
    height: 26px;
    border-radius: 50%;
    background: var(--accent-pink);
  }
  .brand-name {
    font-size: 62px;
    font-weight: 500;
    letter-spacing: 1px;
    line-height: 1;
    color: var(--ink);
  }
  .brand-tagline {
    margin-top: 14px;
    font-size: 22px;
    font-weight: 400;
    color: var(--ink-soft);
  }
  .divider-dots {
    position: absolute;
    left: 470px;
    top: 90px;
    width: 0;
    height: 330px;
    border-left: 5px dotted var(--ink-soft);
  }
  .divider-dots::before {
    content: "";
    position: absolute;
    top: 0;
    left: -5px;
    width: 30px;
    border-top: 5px dotted var(--ink-soft);
  }
  .contact-block {
    position: absolute;
    left: 510px;
    top: 88px;
    width: 460px;
  }
  .person-name {
    margin: 0;
    font-size: 42px;
    font-weight: 600;
    line-height: 1.1;
  }
  .person-role {
    margin: 8px 0 0;
    font-size: 30px;
    font-weight: 400;
    color: var(--ink-soft);
  }
  .contact-list {
    margin: 118px 0 0;
    padding: 0;
    list-style: none;
    font-size: 32px;
    font-weight: 400;
    line-height: 1.32;
  }
  .contact-company {
    font-size: 26px;
    color: var(--accent-pink);
    margin-bottom: 4px;
  }
</style>
</head>
<body>
<main class="canvas">
  <article class="business-card">
    <svg class="card-shape" viewBox="0 0 1000 600" aria-hidden="true">
      <path d="M28,18 Q500,-4 972,18 Q994,20 992,42 Q1004,300 992,558 Q990,580 968,582 Q500,604 32,582 Q10,580 8,558 Q-2,300 8,42 Q10,20 28,18 Z"
            fill="var(--kraft)" stroke="var(--kraft-edge)" stroke-width="2"/>
    </svg>

    <div class="brand-block">
      <div class="brand-mark">
        <span class="brand-dot"></span>
        <span class="brand-name">The Lune Fox</span>
      </div>
      <div class="brand-tagline">Organic &amp; Natural Soaps</div>
    </div>

    <div class="divider-dots"></div>

    <div class="contact-block">
      <h1 class="person-name">Moira Ardley</h1>
      <p class="person-role">Owner</p>
      <ul class="contact-list">
        <li class="contact-company">The Lune Fox Organic &amp; Natural Soaps</li>
        <li class="contact-phone">(555) 014-2287</li>
        <li class="contact-email">Moira@thelunefox.ca</li>
        <li class="contact-web">www.thelunefox.ca</li>
      </ul>
    </div>
  </article>
</main>
</body>
</html>
```